Plate-on-Call Gift Coupon

About Us-
Plate-on-Call is a Tasmanian owned food delivery business which delivers meals from an increasing range of selected restaurants. We provide customers with quality food from reputed restaurants at reasonable delivery charges that meet the highest standards of quality and freshness.
We need some gift coupons/vouchers for our privileged customers. We need three designs which are as follows:
1) 10% OFF
2) FREE DELIVERY
3) FREE DELIVERY when you add any Wine/Beer
Coupons should have following:
Plate-on-Call Logo
Coupon Code: __________
Note:Redeem this coupon on www.plateoncall.com.au

```html
<!DOCTYPE html>
<html lang="en">
<head>
<meta charset="utf-8">
<title>Plate-on-Call Gift Coupon</title>
<link rel="stylesheet" href="https://fonts.googleapis.com/css2?family=Arimo:wght@400;700&family=Open+Sans:wght@600&family=Roboto+Condensed:wght@700&display=swap">
<style>
  :root {
    --orange: #f47a20;
    --ink: #111111;
    --brand-grey: #4a4a4a;
    --paper: #ffffff;
    --cream: #fbecd2;
    --cream-deep: #f6dcae;
    --rule: #3a3a3a;
  }
  * { margin: 0; padding: 0; box-sizing: border-box; }
  html, body { width: 1200px; height: 720px; overflow: hidden; background: var(--paper); }
  .coupon { position: relative; width: 1200px; height: 720px; background: var(--paper); font-family: "Arimo", Arial, sans-serif; color: var(--ink); }
  .rays {
    position: absolute; inset: 0;
    background: radial-gradient(ellipse at 100% 0%, var(--paper) 0%, var(--cream) 45%, var(--cream-deep) 100%);
  }
  .header { position: absolute; left: 0; top: 0; width: 1200px; height: 124px; border-bottom: 4px solid var(--rule); }
  .brand { position: absolute; left: 34px; top: 22px; display: flex; align-items: center; gap: 28px; }
  .brand-dot { width: 72px; height: 72px; border-radius: 50%; background: var(--orange); }
  .brand-name { font-family: "Arimo", Arial, sans-serif; font-weight: 700; font-size: 62px; line-height: 1; color: var(--brand-grey); }
  .frame { position: absolute; left: 12px; top: 141px; width: 1176px; height: 572px; border: 3px solid var(--rule); }
  .offer { position: absolute; left: 50px; font-family: "Roboto Condensed", "Arial Narrow", sans-serif; font-weight: 700; font-size: 76px; line-height: 1; }
  .offer-discount { top: 212px; color: var(--orange); }
  .offer-delivery { top: 310px; }
  .offer-delivery .accent { color: var(--orange); }
  .condition { position: absolute; left: 60px; top: 418px; font-weight: 700; font-size: 72px; line-height: 1; }
  .code { position: absolute; left: 62px; top: 548px; font-family: "Open Sans", Arial, sans-serif; font-weight: 600; font-size: 78px; line-height: 1; display: flex; align-items: flex-end; }
  .code-blank { display: inline-block; width: 400px; height: 4px; background: var(--ink); margin-left: 22px; margin-bottom: 12px; }
  .note { position: absolute; left: 28px; top: 660px; width: 1146px; font-size: 38px; line-height: 1; text-align: justify; text-align-last: justify; }
  .note-label { color: var(--orange); }
</style>
</head>
<body>
<div class="coupon">
  <div class="rays" role="img" aria-label="Soft cream sunburst rays background"></div>
  <header class="header">
    <div class="brand">
      <span class="brand-dot"></span>
      <div class="brand-name">Plate-on-Call</div>
    </div>
  </header>
  <div class="frame"></div>
  <div class="offer offer-discount">10% OFF</div>
  <div class="offer offer-delivery"><span class="accent">FREE</span> DELIVERY</div>
  <div class="condition">when you add any Wine/Beer</div>
  <div class="code">Coupon Code:<span class="code-blank"></span></div>
  <p class="note"><span class="note-label">Note:</span>Redeem this coupon on www.plateoncall.com</p>
</div>
</body>
</html>
```